Business card to be used as a flyer

This business card should do the trick of a full scale flyer , so basicaly from the business card itself we only keep the size and remove the clasical name , position , company name (etc).
This business cards should be , like said above, used as promo tool, being gived to different girls . So base one : the design is girls oriented.
Colors : black background . We will use gold (color) folio for the text.
Attached you have our logo, but this should not be a proiminent part of the design . You can use only the cat head instead.
Target Market(s)
Girls / Women
Contact Information for Business Card
> black background , gold / folio text and elements
> cat head from the logo in a creative way do be displayed
> proieminent text "your path to success starts here"
> contact details phone and website .
www.velmastrand.ro (website) and 0742163958 (phone)

```html
<!DOCTYPE html>
<html lang="en">
<head>
<meta charset="utf-8">
<title>Velmastrand – Promo Card</title>
<link href="https://fonts.googleapis.com/css2?family=Felipa&family=Poiret+One&display=swap" rel="stylesheet">
<style>
  :root {
    --card-black: #000000;
    --gold: #ecc874;
    --gold-light: #f7dc93;
    --gold-deep: #c9953c;
  }
  html, body {
    margin: 0;
    padding: 0;
    width: 686px;
    height: 1200px;
    overflow: hidden;
    background: var(--card-black);
  }
  .card {
    position: relative;
    width: 686px;
    height: 1200px;
    background: var(--card-black);
    color: var(--gold);
  }
  .headline {
    position: absolute;
    top: 140px;
    left: 0;
    width: 100%;
    margin: 0;
    text-align: center;
    font-family: "Felipa", cursive;
    font-weight: 400;
    font-size: 54px;
    line-height: 82px;
    color: var(--gold);
  }
  .badge {
    position: absolute;
    left: 171px;
    top: 446px;
    width: 350px;
    height: 282px;
  }
  .phone {
    position: absolute;
    top: 818px;
    left: 0;
    width: 100%;
    margin: 0;
    text-align: center;
    font-family: "Poiret One", sans-serif;
    font-size: 40px;
    letter-spacing: 5px;
    color: var(--gold-light);
  }
  .brand-mark {
    position: absolute;
    left: 74px;
    top: 918px;
    width: 70px;
    height: 180px;
    display: flex;
    flex-direction: column;
    align-items: center;
    gap: 8px;
  }
  .brand-dot {
    width: 14px;
    height: 14px;
    border-radius: 50%;
    background: var(--gold);
  }
  .brand-name {
    writing-mode: vertical-rl;
    font-family: "Poiret One", sans-serif;
    font-size: 20px;
    letter-spacing: 3px;
    color: var(--gold);
  }
  .visit-label {
    position: absolute;
    top: 956px;
    left: 270px;
    margin: 0;
    font-family: "Poiret One", sans-serif;
    font-size: 21px;
    letter-spacing: 5px;
    color: var(--gold);
  }
  .website {
    position: absolute;
    top: 1000px;
    left: 138px;
    margin: 0;
    font-family: "Poiret One", sans-serif;
    font-size: 44px;
    letter-spacing: 2px;
    color: var(--gold-light);
  }
</style>
</head>
<body>
  <main class="card">
    <h1 class="headline">Your path to<br>Success starts<br>here!</h1>

    <svg class="badge" viewBox="0 0 350 282" role="img" aria-label="Gold foil label frame with a winged woman archer silhouette">
      <defs>
        <linearGradient id="gold-foil" x1="0" y1="0" x2="1" y2="1">
          <stop offset="0" stop-color="#f6d98c"/>
          <stop offset="0.5" stop-color="#e3b356"/>
          <stop offset="1" stop-color="#d39f3f"/>
        </linearGradient>
      </defs>
      <path fill="url(#gold-foil)" d="M40 10 Q100 18 140 14 Q170 12 175 0 Q180 12 210 14 Q250 18 310 10 Q318 30 338 36 Q330 80 336 110 Q342 135 350 141 Q342 147 336 172 Q330 202 338 246 Q318 252 310 272 Q250 264 210 268 Q180 270 175 282 Q170 270 140 268 Q100 264 40 272 Q32 252 12 246 Q20 202 14 172 Q8 147 0 141 Q8 135 14 110 Q20 80 12 36 Q32 30 40 10 Z"/>
    </svg>

    <p class="phone">PHONE: 0742163958</p>

    <div class="brand-mark">
      <span class="brand-dot"></span>
      <span class="brand-name">VELMASTRAND</span>
    </div>

    <p class="visit-label">VISIT US AT</p>
    <p class="website">WWW.VELMASTRAND.RO</p>
  </main>
</body>
</html>
```